Orvel Crest Holdings Ltd
Creative Brief
Dara Kolby
COO
27B Hollin Row, London, E3 9TQ
dk@orvelcrest.co.uk
27b Hollin Row
Just the logo and the company's name on the green background

```html
<!DOCTYPE html>
<html lang="en">
<head>
<meta charset="utf-8">
<title>Orvel Crest Holdings Ltd – Business Card</title>
<link rel="stylesheet" href="https://fonts.googleapis.com/css2?family=Cormorant+Garamond:wght@500&family=Montserrat:wght@400;700&display=swap">
<style>
  :root {
    --backdrop: #d9dadc;
    --forest: #363a2c;
    --forest-light: #3d4232;
    --ink-light: #f3ece0;
    --accent: #d9b878;
    --muted: #d8d3c6;
  }
  * { box-sizing: border-box; margin: 0; padding: 0; }
  html, body { width: 1200px; height: 901px; overflow: hidden; }
  body {
    position: relative;
    background: var(--backdrop);
    font-family: "Montserrat", sans-serif;
  }
  .card {
    position: absolute;
    width: 705px;
    border-radius: 22px;
    overflow: hidden;
  }
  .card--front {
    left: 355px; top: 68px; height: 410px;
    background: linear-gradient(120deg, var(--forest) 0%, var(--forest-light) 50%, var(--forest) 100%);
  }
  .card--back {
    left: 326px; top: 490px; height: 342px;
    background: var(--forest);
  }
  .brand {
    position: absolute;
    display: flex; flex-direction: column; align-items: center;
    font-family: "Cormorant Garamond", serif;
    font-weight: 500;
    text-transform: uppercase;
    text-align: center;
    line-height: 1;
    white-space: nowrap;
    color: #ffffff;
  }
  .brand__mark {
    border-radius: 50%;
    border-style: solid;
    border-color: var(--accent);
  }
  .card--front .brand {
    left: 0; right: 0; top: 62px;
  }
  .card--front .brand__mark { width: 148px; height: 148px; border-width: 3px; margin-bottom: 26px; }
  .card--front .brand__name { font-size: 64px; letter-spacing: 1px; }
  .card--front .brand__sub { font-size: 24px; letter-spacing: 1px; margin-top: 8px; color: var(--accent); }

  .card--back .brand {
    left: 30px; width: 240px; top: 92px;
  }
  .card--back .brand__mark { width: 96px; height: 96px; border-width: 2px; margin-bottom: 18px; }
  .card--back .brand__name { font-size: 32px; }
  .card--back .brand__sub { font-size: 14px; margin-top: 5px; color: var(--accent); }

  .divider {
    position: absolute;
    left: 273px; top: 70px;
    width: 1px; height: 200px;
    background: var(--muted);
    opacity: .7;
  }
  .contact {
    position: absolute;
    left: 297px; top: 68px;
    color: var(--ink-light);
  }
  .contact__name { font-weight: 700; font-size: 25px; color: var(--accent); letter-spacing: .5px; }
  .contact__role { font-size: 13px; margin-top: 2px; }
  .contact__address { font-size: 13px; line-height: 22px; margin-top: 28px; }
  .contact__list { list-style: none; margin-top: 16px; }
  .contact__list li { display: flex; align-items: center; font-size: 13px; height: 21px; }
  .contact__list svg { width: 12px; height: 12px; margin-right: 10px; fill: var(--accent); flex: none; }
</style>
</head>
<body>
  <section class="card card--front" aria-label="Card front">
    <div class="brand">
      <span class="brand__mark"></span>
      <span class="brand__name">Orvel Crest</span>
      <span class="brand__sub">Holdings Ltd.</span>
    </div>
  </section>

  <section class="card card--back" aria-label="Card back">
    <div class="brand">
      <span class="brand__mark"></span>
      <span class="brand__name">Orvel Crest</span>
      <span class="brand__sub">Holdings Ltd.</span>
    </div>
    <div class="divider"></div>
    <div class="contact">
      <h1 class="contact__name">DARA KOLBY</h1>
      <p class="contact__role">COO</p>
      <p class="contact__address">27B Hollin Row,<br>London, E3 9TQ</p>
      <ul class="contact__list">
        <li><svg viewBox="0 0 12 12"><path d="M2.5 1h2l1 2.6-1.3 1a6.5 6.5 0 0 0 3.2 3.2l1-1.3L11 7.5v2c0 .8-.7 1.5-1.5 1.5A8.5 8.5 0 0 1 1 2.5C1 1.7 1.7 1 2.5 1z"/></svg>+44 (0)20 7946 0312</li>
        <li><svg viewBox="0 0 12 12"><rect x="3" y="0.5" width="6" height="11" rx="1.2"/></svg>+44 (0)77 0090 0614</li>
        <li><svg viewBox="0 0 12 12"><path d="M0.5 2.5h11v7h-11z M0.5 2.5 6 6.5l5.5-4" /></svg>dk@orvelcrest.co.uk</li>
        <li><svg viewBox="0 0 12 12"><circle cx="6" cy="6" r="5.5"/></svg>27b Hollin Row</li>
      </ul>
    </div>
  </section>
</body>
</html>
```